New Townhome community needs for sale sign.

need a 4 foot by 8 foot banner to put on building listing newly constructed townhomes as "coming soon" to market. Construction is scheduled to be completed Dec 2024. Sale of units will begin Spring of 2025.
6 individual townhome units each 2,000 square feet. each unit is 3 bedroom 2.5 bathroom with 2 car garage and each has a rooftop "sky lounge" with amazing views. Gated community. Units available for sale Spring of 2025. Real estate company selling units will be QVR & Partners. Will need QVR & Partners Logo on the banner. Would like to keep with the same blue color scheme as the QVR & Partners logo. phone number on banner to be 602-555-4179. web qvrpartnersx.com.

```html
<!DOCTYPE html>
<html lang="en">
<head>
<meta charset="utf-8">
<title>QVR &amp; Partners – Coming Soon Banner</title>
<link rel="stylesheet" href="https://fonts.googleapis.com/css2?family=Barlow+Condensed:wght@500&display=swap">
<style>
  :root {
    --backdrop: #c3c3c3;
    --paper: #ffffff;
    --blue-deep: #1d6ba3;
    --blue-bright: #25a7dd;
    --bar-blue: #1e6a9c;
    --charcoal: #3a3a3c;
    --ink: #2b2b2d;
  }
  html, body {
    margin: 0;
    width: 1200px;
    height: 1200px;
    overflow: hidden;
    background: var(--backdrop);
  }
  .banner {
    position: absolute;
    left: 70px;
    top: 335px;
    width: 1060px;
    height: 529px;
    background: var(--paper);
    overflow: hidden;
    font-family: "Barlow Condensed", "Arial Narrow", sans-serif;
    font-weight: 500;
  }
  .banner__shapes {
    position: absolute;
    inset: 0;
    width: 100%;
    height: 100%;
  }
  .headline {
    position: absolute;
    right: 64px;
    top: 52px;
    margin: 0;
    font-size: 168px;
    line-height: 1;
    font-weight: 500;
    letter-spacing: -0.5px;
    color: var(--paper);
    white-space: nowrap;
  }
  .completion-note {
    position: absolute;
    right: 58px;
    top: 218px;
    margin: 0;
    font-size: 33.5px;
    line-height: 1;
    color: var(--paper);
    white-space: nowrap;
  }
  .sale-note {
    position: absolute;
    right: 59px;
    top: 376px;
    margin: 0;
    font-size: 32px;
    line-height: 1;
    color: var(--ink);
    white-space: nowrap;
  }
  .contact-bar {
    position: absolute;
    left: 530px;
    right: 0;
    top: 436px;
    height: 58px;
    background: var(--bar-blue);
    color: var(--paper);
    font-size: 34px;
    display: flex;
    align-items: center;
    justify-content: flex-end;
    padding-right: 59px;
    box-sizing: border-box;
    white-space: nowrap;
  }
  .brand {
    position: absolute;
    left: 60px;
    top: 414px;
    display: flex;
    align-items: center;
    gap: 16px;
  }
  .brand__mark {
    width: 80px;
    height: 80px;
    background: var(--blue-bright);
  }
  .brand__name {
    font-size: 58px;
    line-height: 1;
    color: var(--charcoal);
    white-space: nowrap;
  }
</style>
</head>
<body>
  <section class="banner">
    <svg class="banner__shapes" viewBox="0 0 848 423" preserveAspectRatio="none" aria-hidden="true">
      <defs>
        <linearGradient id="sky-blue" x1="0" y1="0" x2="1" y2="0">
          <stop offset="0" stop-color="var(--blue-deep)"/>
          <stop offset="1" stop-color="var(--blue-bright)"/>
        </linearGradient>
      </defs>
      <polygon class="shape-blue" points="18,0 848,0 848,226 300,298" fill="url(#sky-blue)"/>
      <polygon class="shape-charcoal" points="0,32 300,298 0,236" fill="var(--charcoal)"/>
    </svg>

    <h1 class="headline">COMING SOON</h1>
    <p class="completion-note">CONSTRUCTION IS SCHEDULED TO BE COMPLETED DEC 2024.</p>
    <p class="sale-note">SALE OF UNITS WILL BEGIN SPRING OF 2025.</p>

    <div class="brand">
      <span class="brand__mark"></span>
      <span class="brand__name">QVR &amp; Partners</span>
    </div>

    <div class="contact-bar">602-555-4179 | QVRPARTNERSX.COM</div>
  </section>
</body>
</html>
```